Business Card Design Project

I have established a company called "Tidewell" which is a business specialising in psychotherapy/counselling , predominantly for anxiety & depression.

My name is Mel....hence, the Tidewell link. However, Tidewell was also chosen for its reference to green shoots of growth/recovery.

Tidewell is to be "upmarket" and highly professional. I'm keen for the style and colours to reflect this.....taupe/grey with navy/black script, for example.....NO primary colours.

My name needs to be on the card and my mobile number. Not sure, but suspect it should also have my qualifications ( BA (Psych) & BSc (Hons) Psychology). Mobile number 0463 918 207.

```html
<!DOCTYPE html>
<html lang="en">
<head>
<meta charset="utf-8">
<title>Tidewell – Business Card</title>
<link rel="stylesheet" href="https://fonts.googleapis.com/css2?family=Arimo:wght@400;700&display=swap">
<style>
  :root {
    --stage: #ebebeb;
    --card-light: #e6e4e2;
    --card-light-soft: #d9d7d5;
    --card-dark: #4a4745;
    --card-dark-soft: #3f3c3a;
    --ink: #3a3836;
    --ink-soft: #55524f;
    --taupe: #b3a697;
  }
  * { margin: 0; padding: 0; box-sizing: border-box; }
  html, body {
    width: 1200px;
    height: 1000px;
    overflow: hidden;
    background: var(--stage);
    font-family: "Arimo", Arial, sans-serif;
  }
  .stage {
    width: 1200px;
    height: 1000px;
    display: flex;
    align-items: center;
    justify-content: center;
    gap: 60px;
  }
  .card {
    position: relative;
    width: 525px;
    height: 300px;
    overflow: hidden;
    box-shadow: 0 6px 18px rgba(0,0,0,0.12);
  }
  .card-texture {
    position: absolute;
    inset: 0;
  }
  .card--front { background: var(--card-light); }
  .card--front .card-texture {
    background: radial-gradient(ellipse at 70% 30%, var(--card-light) 0%, var(--card-light-soft) 100%);
  }
  .card--back { background: var(--card-dark); }
  .card--back .card-texture {
    background: radial-gradient(ellipse at 35% 40%, var(--card-dark) 0%, var(--card-dark-soft) 100%);
  }
  .card-content { position: relative; }

  .wordmark-name {
    font-weight: 700;
    letter-spacing: -0.5px;
    line-height: 1;
  }
  .wordmark-tagline {
    font-weight: 400;
    line-height: 1;
  }

  /* front */
  .card--front .card-content {
    padding: 82px 0 0 110px;
    color: var(--ink);
  }
  .card--front .wordmark-name { font-size: 44px; color: var(--ink); }
  .card--front .wordmark-tagline { font-size: 10px; color: var(--ink-soft); margin: 4px 0 0 62px; }
  .holder { margin: 26px 0 0 62px; }
  .holder-name { font-size: 18px; font-weight: 400; color: var(--ink); }
  .holder-quals { font-size: 10px; color: var(--ink-soft); margin-top: 4px; }
  .holder-contact { font-size: 10px; color: var(--ink-soft); margin-top: 14px; line-height: 1.55; }

  /* back */
  .card--back .card-content {
    height: 300px;
    display: flex;
    flex-direction: column;
    justify-content: center;
    padding-left: 70px;
  }
  .card--back .wordmark-name { font-size: 82px; color: var(--taupe); }
  .card--back .wordmark-tagline { font-size: 16px; color: var(--taupe); margin: 6px 0 0 110px; }
</style>
</head>
<body>
  <main class="stage">
    <section class="card card--front" aria-label="Card front">
      <div class="card-texture" role="img" aria-label="Soft pale grey bokeh circle pattern"></div>
      <div class="card-content">
        <div class="wordmark">
          <div class="wordmark-name">Tidewell</div>
          <div class="wordmark-tagline">predominantly for anxiety &amp; depression</div>
        </div>
        <div class="holder">
          <div class="holder-name">Mel Ashby</div>
          <div class="holder-quals">BA (Psych) &amp; BSc (Hons) Psychology</div>
          <div class="holder-contact">
            M: 0463 918 207<br>
            E: mel@tidewell.com.au | W: www.YourWebsite.com
          </div>
        </div>
      </div>
    </section>

    <section class="card card--back" aria-label="Card back">
      <div class="card-texture" role="img" aria-label="Soft dark grey bokeh circle pattern"></div>
      <div class="card-content">
        <div class="wordmark">
          <div class="wordmark-name">Tidewell</div>
          <div class="wordmark-tagline">predominantly for anxiety &amp; depression</div>
        </div>
      </div>
    </section>
  </main>
</body>
</html>
```